Author needs design for self-help relationship book

I need a book cover design for a self-help handbook on relationships called 'Where Partners Find Calm Harbours - Letters From Quiet Mornings". The design should appeal in the main to young couples anywhere in the world.

```html
<!DOCTYPE html>
<html lang="en">
<head>
<meta charset="utf-8">
<title>Where Partners Find Calm Harbours – Book Cover</title>
<link href="https://fonts.googleapis.com/css2?family=Cinzel:wght@400;500&family=Open+Sans:wght@400&display=swap" rel="stylesheet">
<style>
  :root {
    --sky-top: #f5ead0;
    --sky-mid: #f0dcae;
    --horizon: #e9c47e;
    --sea-glow: #d9b26a;
    --sea-deep: #8f8466;
    --sand: #c7ab83;
    --sand-dark: #a98d68;
    --title-red: #a3221a;
    --subtitle-ink: #4a4036;
    --author-ink: #3b2c20;
    --ghost: rgba(120, 100, 70, 0.18);
  }
  html, body {
    margin: 0;
    padding: 0;
    width: 800px;
    height: 1200px;
    overflow: hidden;
    background: #ffffff;
  }
  .cover {
    position: relative;
    width: 800px;
    height: 1200px;
    overflow: hidden;
  }
  .cover-photo {
    position: absolute;
    inset: 0;
    background:
      radial-gradient(ellipse 260px 180px at 360px 600px, rgba(255, 240, 200, 0.75), rgba(255, 240, 200, 0) 70%),
      linear-gradient(to bottom,
        var(--sky-top) 0%,
        var(--sky-mid) 28%,
        var(--horizon) 44%,
        var(--sea-glow) 50%,
        var(--sea-deep) 68%,
        var(--sand) 80%,
        var(--sand-dark) 100%);
  }
  .title-art {
    position: absolute;
    top: 0;
    left: 0;
    width: 800px;
    height: 420px;
  }
  .title-top,
  .title-main,
  .title-echo {
    font-family: "Cinzel", serif;
    font-weight: 400;
  }
  .title-top,
  .title-main { fill: var(--title-red); }
  .title-echo {
    fill: none;
    stroke: var(--ghost);
    stroke-width: 1.5;
  }
  .tagline {
    position: absolute;
    top: 222px;
    left: 0;
    width: 800px;
    margin: 0;
    font-family: "Open Sans", sans-serif;
    font-size: 31px;
    letter-spacing: 3px;
    color: var(--subtitle-ink);
    text-align: center;
    line-height: 1;
  }
  .author {
    position: absolute;
    bottom: 34px;
    left: 0;
    width: 800px;
    margin: 0;
    font-family: "Cinzel", serif;
    font-weight: 400;
    font-size: 46px;
    letter-spacing: 4px;
    color: var(--author-ink);
    text-align: center;
    line-height: 1;
  }
</style>
</head>
<body>
  <main class="cover">
    <div class="cover-photo" role="img" aria-label="Photograph of a couple in silhouette on a beach at sunset, their arms joined overhead to form a heart shape against the golden sea and sky"></div>

    <svg class="title-art" viewBox="0 0 800 420" role="img" aria-label="Where Partners Find Calm Harbours">
      <text class="title-echo" x="22" y="390" font-size="120" textLength="400" lengthAdjust="spacingAndGlyphs" aria-hidden="true">HARBOURS</text>
      <text class="title-top" x="150" y="78" font-size="38" textLength="610" lengthAdjust="spacingAndGlyphs">WHERE PARTNERS FIND CALM</text>
      <text class="title-main" x="22" y="204" font-size="160" textLength="756" lengthAdjust="spacingAndGlyphs">HARBOURS</text>
    </svg>

    <p class="tagline">Letters From Quiet Mornings</p>

    <p class="author">DANIEL WHITCOMBE</p>
  </main>
</body>
</html>
```